Telmoro Business Card

I already have the conplay logo. I need to develop a professional business card layout

Target Market(s)

Business

Industry/Entity Type

Business

Contact Information for Business Card

Company Name: Telmoro Limited

Font styles to use
Sans Serif

Colors

Designer to choose colors to be used in the design.

Requirements
Must have
• Use current logo
• Need two card size options:
• Small Card: 70mm x 28mm (Landscape)
• Square Card: 65mm x 65mm
Nice to have
• I will need 8-10 files for each name, number and email address (details to follow)

```html
<!DOCTYPE html>
<html lang="en">
<head>
<meta charset="utf-8">
<title>Telmoro Limited – Business Card</title>
<link rel="stylesheet" href="https://fonts.googleapis.com/css2?family=Oxygen:wght@300;400;700&display=swap">
<style>
  :root {
    --backdrop: #e6e6e8;
    --card: #ffffff;
    --card-shade: #f1f2f4;
    --navy: #14264a;
    --brand-blue: #1565c0;
    --blue-deep: #0a66c2;
    --blue-mid: #2b8fd9;
    --blue-light: #7fcdf0;
  }
  * { box-sizing: border-box; margin: 0; padding: 0; }
  html, body {
    width: 1200px;
    height: 877px;
    overflow: hidden;
    background: var(--backdrop);
    font-family: "Oxygen", "Helvetica Neue", Arial, sans-serif;
  }
  .business-card {
    position: absolute;
    left: 40px;
    top: 118px;
    width: 1120px;
    height: 640px;
    background: linear-gradient(135deg, var(--card) 0%, var(--card-shade) 100%);
    box-shadow: 0 6px 18px rgba(0, 0, 0, 0.12);
    overflow: hidden;
  }
  .pattern {
    position: absolute;
  }
  .pattern-top {
    left: 0;
    top: 0;
    width: 560px;
    height: 230px;
    background: linear-gradient(160deg, var(--blue-deep) 0%, var(--blue-mid) 30%, var(--blue-light) 60%, rgba(127, 205, 240, 0) 90%);
    clip-path: polygon(0 0, 100% 0, 100% 15%, 55% 55%, 10% 100%, 0 100%);
  }
  .pattern-bottom {
    right: 0;
    bottom: 0;
    width: 590px;
    height: 180px;
    background: linear-gradient(340deg, var(--blue-deep) 0%, var(--blue-mid) 30%, var(--blue-light) 60%, rgba(127, 205, 240, 0) 90%);
    clip-path: polygon(100% 0, 100% 100%, 0 100%, 0 85%, 45% 45%, 90% 0);
  }
  .brand-name {
    position: absolute;
    left: 35px;
    top: 318px;
    font-size: 92px;
    font-weight: 700;
    letter-spacing: 1px;
    color: var(--brand-blue);
    text-transform: uppercase;
    line-height: 1;
  }
  .divider {
    position: absolute;
    left: 563px;
    top: 170px;
    width: 2px;
    height: 290px;
    background: linear-gradient(180deg, rgba(20, 38, 74, 0) 0%, rgba(20, 38, 74, 0.12) 20%, rgba(20, 38, 74, 0.12) 80%, rgba(20, 38, 74, 0) 100%);
  }
  .company-name {
    position: absolute;
    left: 592px;
    top: 212px;
    font-size: 47px;
    font-weight: 300;
    color: var(--navy);
    text-transform: uppercase;
    letter-spacing: 1px;
    line-height: 1;
  }
  .company-name strong { font-weight: 400; }
  .contact-list {
    position: absolute;
    left: 603px;
    top: 305px;
    list-style: none;
  }
  .contact-item {
    display: flex;
    align-items: center;
    height: 35px;
    font-size: 19px;
    font-weight: 700;
    color: var(--navy);
  }
  .contact-icon {
    width: 18px;
    height: 18px;
    margin-right: 12px;
    fill: var(--navy);
    flex: none;
  }
</style>
</head>
<body>
  <main class="business-card">
    <div class="pattern pattern-top" role="img" aria-label="Decorative pattern of scattered blue squares"></div>
    <div class="pattern pattern-bottom" role="img" aria-label="Decorative pattern of scattered blue squares"></div>

    <div class="brand-name">Telmoro</div>

    <div class="divider"></div>

    <h1 class="company-name">Telmoro <strong>Limited</strong></h1>

    <ul class="contact-list">
      <li class="contact-item">
        <svg class="contact-icon" viewBox="0 0 24 24" aria-hidden="true"><path d="M12 2a8 8 0 0 0-8 8v6a3 3 0 0 0 3 3h1v-8H6v-1a6 6 0 0 1 12 0v1h-2v8h1a3 3 0 0 0 3-3v-6a8 8 0 0 0-8-8z"/></svg>
        name
      </li>
      <li class="contact-item">
        <svg class="contact-icon" viewBox="0 0 24 24" aria-hidden="true"><path d="M6.6 10.8a15.1 15.1 0 0 0 6.6 6.6l2.2-2.2a1 1 0 0 1 1-.25 11.4 11.4 0 0 0 3.6.57 1 1 0 0 1 1 1V20a1 1 0 0 1-1 1A17 17 0 0 1 3 4a1 1 0 0 1 1-1h3.5a1 1 0 0 1 1 1c0 1.25.2 2.45.57 3.6a1 1 0 0 1-.25 1z"/></svg>
        +00 1234 5678 9012
      </li>
      <li class="contact-item">
        <svg class="contact-icon" viewBox="0 0 24 24" aria-hidden="true"><path d="M2 5h20v14H2z M4 7v.5l8 5 8-5V7l-8 5z" fill-rule="evenodd"/></svg>
        contact@websitename.com
      </li>
      <li class="contact-item">
        <svg class="contact-icon" viewBox="0 0 24 24" aria-hidden="true"><path d="M12 2a7 7 0 0 0-7 7c0 5.25 7 13 7 13s7-7.75 7-13a7 7 0 0 0-7-7zm0 9.5A2.5 2.5 0 1 1 12 6.5a2.5 2.5 0 0 1 0 5z"/></svg>
        123 Dummy Road, Lorem Ipsum, Country
      </li>
    </ul>
  </main>
</body>
</html>
```